Re-Design WP Site BrightPebbles.info

Site Re-design. Also Need a Button for contact on main page. Need Great Looking products re designed. Also bonus if you can install a site SEO checker on the site.

BrightPebbles.info

```html
<!DOCTYPE html>
<html lang="en">
<head>
<meta charset="utf-8">
<title>BrightPebbles.info</title>
<link href="https://fonts.googleapis.com/css2?family=Montserrat:wght@400;500;600;700&display=swap" rel="stylesheet">
<style>
:root{
  --purple:#6b2fe6;
  --indigo:#4a3ce6;
  --violet:#9a2fe0;
  --ink:#1f1f2b;
  --body:#3a3a46;
  --muted:#7a7a88;
  --line:#e4e4ee;
  --pale:#f1f5fd;
  --night:#1b0f3b;
  --white:#ffffff;
}
*{box-sizing:border-box;margin:0;padding:0}
html,body{width:1200px;height:5029px;overflow:hidden}
body{position:relative;font-family:"Montserrat",sans-serif;color:var(--body);background:var(--white)}
.abs{position:absolute}
.section-title{position:absolute;left:0;width:1200px;text-align:center;font-size:38px;font-weight:500;color:var(--ink);letter-spacing:.5px}
.section-title::after{content:"";display:block;width:58px;height:3px;background:var(--purple);margin:8px auto 0}
.btn{position:absolute;display:flex;align-items:center;justify-content:center;border-radius:20px;font-size:14px;font-weight:600;letter-spacing:.3px;text-transform:uppercase}
.btn-primary{background:linear-gradient(90deg,var(--indigo),var(--violet));color:var(--white);border:2px solid var(--white)}
.btn-light{background:var(--white);color:var(--purple)}
.more{font-size:14px;font-weight:600;color:var(--indigo);text-transform:uppercase}

/* hero */
.hero{position:absolute;left:0;top:0;width:1200px;height:656px;background:radial-gradient(circle at 78% 50%,#6a2aa8 0%,#3c1868 40%,#1a0c2c 100%)}
.hero-photo{position:absolute;left:0;top:330px;width:560px;height:326px;background:linear-gradient(160deg,rgba(90,40,140,.0),rgba(120,60,150,.35))}
.hero-visual{position:absolute;left:570px;top:70px;width:610px;height:580px;border-radius:50%;background:radial-gradient(circle at 50% 50%,rgba(210,170,255,.35) 0%,rgba(140,70,210,.2) 45%,rgba(60,24,104,0) 72%)}
.brand{position:absolute;color:var(--white)}
.brand-name{font-size:26px;font-weight:400;letter-spacing:2px}
.brand-tag{font-size:11px;margin-top:2px}
.nav{position:absolute;top:34px;left:0;width:1200px;height:20px}
.nav a{position:absolute;transform:translateX(-50%);color:var(--white);font-size:15px;font-weight:500;text-decoration:none}
.hero h1{position:absolute;left:100px;top:222px;width:520px;font-size:49px;line-height:50px;font-weight:600;color:var(--white);letter-spacing:1px}
.hero p{position:absolute;left:100px;top:334px;width:460px;font-size:15px;line-height:30px;color:var(--white)}
.dots{position:absolute;top:611px;left:552px;display:flex;gap:15px}
.dots span{width:12px;height:12px;border-radius:50%;border:2px solid var(--white)}
.dots span.on{background:var(--white)}

/* solutions */
.card{position:absolute;width:316px;background:var(--white);box-shadow:0 2px 10px rgba(40,30,90,.10);text-align:center}
.card .photo{position:absolute;left:0;top:0;width:316px;height:207px}
.card .icon{position:absolute;left:128px;top:182px;width:60px;height:60px;border-radius:50%;background:var(--purple);border:4px solid var(--white);display:flex;align-items:center;justify-content:center}
.card h3{position:absolute;top:253px;left:0;width:100%;font-size:18px;font-weight:600;color:var(--ink)}
.card h3::after{content:"";display:block;width:46px;height:2px;background:var(--purple);margin:10px auto 0}
.card p{position:absolute;top:296px;left:14px;width:288px;font-size:13px;line-height:24px}
.card .more{position:absolute;top:378px;left:0;width:100%}

/* about */
.about{position:absolute;left:0;top:1772px;width:1200px;height:520px;background:linear-gradient(100deg,#8e2be0 0%,#5a38e4 55%,#4a3ce6 100%)}
.about-ghost{position:absolute;left:-110px;top:230px;transform:rotate(-90deg);font-size:120px;font-weight:700;color:rgba(255,255,255,.06);letter-spacing:4px}
.about-ring{position:absolute;left:123px;top:52px;width:418px;height:418px;border-radius:50%;background:#3a1a8a}
.about-photo{position:absolute;left:123px;top:52px;width:410px;height:410px;border-radius:50%;background:linear-gradient(150deg,#d9d6e6,#7a6e8e 60%,#3a2d4e)}
.about h2{position:absolute;left:660px;top:76px;font-size:38px;font-weight:500;color:var(--white)}
.about h2::after{content:"";display:block;width:48px;height:2px;background:var(--white);margin-top:10px}
.about p{position:absolute;left:660px;top:152px;width:440px;font-size:14px;line-height:28.5px;color:var(--white);text-align:justify}

/* videos */
.video{position:absolute;top:2472px;width:483px;height:334px;border-radius:4px}
.play{position:absolute;left:50%;top:50%;width:56px;height:56px;margin:-28px 0 0 -28px;border-radius:50%;background:var(--white);display:flex;align-items:center;justify-content:center}

/* testimonials */
.clients{position:absolute;left:0;top:2903px;width:1200px;height:437px;background:var(--pale)}
.quote{position:absolute;left:170px;top:183px;width:860px;text-align:center;font-size:19px;line-height:34px;color:var(--ink)}
.arrow{position:absolute;top:188px;width:42px;height:42px;border-radius:50%;background:#e3e6f8;display:flex;align-items:center;justify-content:center}
.avatar{position:absolute;left:490px;top:289px;width:62px;height:62px;border-radius:50%;background:linear-gradient(160deg,#cfd5e4,#7d8699)}
.who{position:absolute;left:566px;top:297px}
.who b{display:block;font-size:21px;font-weight:500;color:var(--ink)}
.who span{font-size:13px;color:var(--muted)}

/* blog */
.post{position:absolute;top:3512px;width:316px;height:406px;background:var(--white);box-shadow:0 2px 10px rgba(40,30,90,.10)}
.post .photo{position:absolute;left:10px;top:10px;width:296px;height:197px}
.post .date{position:absolute;left:10px;top:181px;background:var(--purple);color:var(--white);font-size:12px;padding:6px 14px}
.post h3{position:absolute;left:10px;top:232px;width:296px;font-size:17px;line-height:24px;font-weight:600;color:var(--ink)}
.post p{position:absolute;left:10px;top:288px;width:296px;font-size:13px;line-height:24.5px}
.post .more{position:absolute;left:10px;top:372px}

/* contact */
.contact{position:absolute;left:0;top:4015px;width:1200px;height:632px;background:linear-gradient(90deg,#ffffff 0%,#f6f6f6 55%,#e9e9ec 100%)}
.contact-photo{position:absolute;left:760px;top:0;width:440px;height:632px;background:linear-gradient(160deg,#f0f0f2,#c9cbd2 50%,#8e8f96)}
.contact-leaf{position:absolute;left:0;top:0;width:110px;height:150px;background:linear-gradient(160deg,#3d7a2e,#9ac07e);border-bottom-right-radius:110px;opacity:.85}
.contact h2{position:absolute;left:100px;top:138px;font-size:40px;font-weight:500;color:var(--ink)}
.contact .lead{position:absolute;left:100px;top:212px;font-size:14px}
.field{position:absolute;height:49px;border:1px solid #d9d9e2;background:var(--white);font-size:13px;color:var(--muted);padding:15px 20px}

/* footer */
.footer{position:absolute;left:0;top:4647px;width:1200px;height:382px;background:var(--night);color:var(--white)}
.social{position:absolute;top:134px;width:34px;height:34px;border-radius:50%;background:var(--purple)}
.col{position:absolute;top:68px}
.col h4{font-size:17px;font-weight:600;margin-bottom:20px}
.col h4::after{content:"";display:block;width:32px;height:2px;background:var(--purple);margin-top:4px}
.col li{list-style:none;font-size:13px;height:34.5px}
.info{display:flex;gap:10px;font-size:13px;line-height:18px;margin-bottom:18px}
.rule{position:absolute;left:100px;top:313px;width:1000px;height:1px;background:rgba(255,255,255,.15)}
.copy{position:absolute;left:0;top:340px;width:1200px;text-align:center;font-size:13px}
.top-btn{position:absolute;left:1134px;top:225px;width:42px;height:42px;border-radius:50%;background:var(--purple);display:flex;align-items:center;justify-content:center}
.top-label{position:absolute;left:1124px;top:275px;font-size:9px;font-weight:600}
</style>
</head>
<body>

<header class="hero">
  <div class="hero-photo" role="img" aria-label="Photo of a hand touching a glowing digital interface"></div>
  <div class="hero-visual" role="img" aria-label="Illustration of a software cloud linked to devices and servers"></div>
  <div class="brand" style="left:101px;top:18px">
    <div class="brand-name">BRIGHT PEBBLES.info</div>
    <div class="brand-tag">Cutting Edge Business Services to Help You Shine Bright</div>
  </div>
  <nav class="nav">
    <a style="left:622px">HOME</a>
    <a style="left:718px">SHOP</a>
    <a style="left:835px">SOLUTIONS</a>
    <a style="left:950px">BLOG</a>
    <a style="left:1059px">CONTACT</a>
  </nav>
  <h1>WE ARE DIGITAL INNOVATORS</h1>
  <p>We’re a studio of creators inventing unique and effective IT applications providing solutions that solve real world problems.</p>
  <div class="btn btn-primary" style="left:100px;top:440px;width:162px;height:38px">Get Started »</div>
  <div class="dots"><span></span><span></span><span class="on"></span><span></span></div>
</header>

<h2 class="section-title" style="top:737px">OUR SOLUTIONS</h2>

<article class="card" style="left:100px;top:823px;height:416px">
  <div class="photo" role="img" aria-label="Photo of a person at a laptop with ad graphics" style="background:linear-gradient(150deg,#c8a78a,#5f5f6e)"></div>
  <div class="icon"><svg width="26" height="26" viewBox="0 0 26 26" fill="none" stroke="#fff" stroke-width="2"><rect x="3" y="5" width="20" height="14" rx="2"/><line x1="9" y1="23" x2="17" y2="23"/></svg></div>
  <h3>ADVERTISING</h3>
  <p>Lorem ipsum dolor sit amet, consectetur adipiscing elit, sed do eiusmod tempor incididunt ut labore et dolore</p>
  <div class="more">Learn More »</div>
</article>
<article class="card" style="left:442px;top:823px;height:416px">
  <div class="photo" role="img" aria-label="Photo of a businessman holding a tablet with rating stars" style="background:linear-gradient(160deg,#3b5f8e,#15243e)"></div>
  <div class="icon"><svg width="26" height="26" viewBox="0 0 26 26" fill="none" stroke="#fff" stroke-width="2"><circle cx="13" cy="10" r="7"/><polyline points="8,16 6,24 13,21 20,24 18,16"/></svg></div>
  <h3>REPUTATION</h3>
  <p>Lorem ipsum dolor sit amet, consectetur adipiscing elit, sed do eiusmod tempor incididunt ut labore et dolore</p>
  <div class="more">Learn More »</div>
</article>
<article class="card" style="left:784px;top:823px;height:416px">
  <div class="photo" role="img" aria-label="Photo of hands typing beneath a glowing cloud graphic" style="background:linear-gradient(160deg,#cfe3f5,#3e6f9e)"></div>
  <div class="icon"><svg width="26" height="26" viewBox="0 0 26 26" fill="none" stroke="#fff" stroke-width="2"><rect x="6" y="3" width="14" height="20" rx="2"/><line x1="9" y1="9" x2="17" y2="9"/><line x1="9" y1="13" x2="17" y2="13"/><line x1="9" y1="17" x2="17" y2="17"/></svg></div>
  <h3>LISTINGS</h3>
  <p>Lorem ipsum dolor sit amet, consectetur adipiscing elit, sed do eiusmod tempor incididunt ut labore et dolore</p>
  <div class="more">Learn More »</div>
</article>
<article class="card" style="left:100px;top:1266px;height:416px">
  <div class="photo" role="img" aria-label="Photo of a team sketching website wireframes" style="background:linear-gradient(150deg,#7fa5c9,#c9b79e)"></div>
  <div class="icon"><svg width="26" height="26" viewBox="0 0 26 26" fill="none" stroke="#fff" stroke-width="2"><rect x="3" y="4" width="20" height="18" rx="2"/><line x1="3" y1="9" x2="23" y2="9"/><rect x="7" y="12" width="5" height="6"/><line x1="15" y1="13" x2="19" y2="13"/><line x1="15" y1="17" x2="19" y2="17"/></svg></div>
  <h3>WEBSITE</h3>
  <p>Lorem ipsum dolor sit amet, consectetur adipiscing elit, sed do eiusmod tempor incididunt ut labore et dolore</p>
  <div class="more">Learn More »</div>
</article>
<article class="card" style="left:442px;top:1266px;height:416px">
  <div class="photo" role="img" aria-label="Photo of a laptop showing search optimisation notes" style="background:linear-gradient(160deg,#d8d2c4,#7b6a55)"></div>
  <div class="icon"><svg width="26" height="26" viewBox="0 0 26 26" fill="none" stroke="#fff" stroke-width="2"><circle cx="11" cy="11" r="7"/><line x1="16" y1="16" x2="23" y2="23"/></svg></div>
  <h3>SEO</h3>
  <p>Lorem ipsum dolor sit amet, consectetur adipiscing elit, sed do eiusmod tempor incididunt ut labore et dolore</p>
  <div class="more">Learn More »</div>
</article>
<article class="card" style="left:784px;top:1266px;height:416px">
  <div class="photo" role="img" aria-label="Photo of a person using social media on a phone and laptop" style="background:linear-gradient(160deg,#b9c9e2,#5d7396)"></div>
  <div class="icon"><svg width="26" height="26" viewBox="0 0 26 26" fill="none" stroke="#fff" stroke-width="2"><circle cx="7" cy="13" r="3"/><circle cx="19" cy="6" r="3"/><circle cx="19" cy="20" r="3"/><line x1="10" y1="12" x2="16" y2="7"/><line x1="10" y1="14" x2="16" y2="19"/></svg></div>
  <h3>SOCIAL</h3>
  <p>Lorem ipsum dolor sit amet, consectetur adipiscing elit, sed do eiusmod tempor incididunt ut labore et dolore</p>
  <div class="more">Learn More »</div>
</article>

<section class="about">
  <div class="about-ghost">ABOUT</div>
  <div class="about-ring"></div>
  <div class="about-photo" role="img" aria-label="Photo of two colleagues looking at a tablet together"></div>
  <h2>ABOUT US</h2>
  <p>BrightPebbles.info is a saas company that provides software solutions to businesses of all sizes. We offer a variety of saas software products that can help your business improve its productivity and efficiency. Our saas business products are easy to use and our team is always available to help you get the most out of them. Use our free trial to learn more about our software company how we can help your business grow.</p>
  <div class="btn btn-light" style="left:660px;top:396px;width:162px;height:37px">Get Started »</div>
</section>

<h2 class="section-title" style="top:2374px">OUR VIDEOS</h2>
<div class="video" style="left:100px;background:linear-gradient(150deg,#c9c5bf,#6d6a66 60%,#3f3d3b)" role="img" aria-label="Video still of a team celebrating at their laptops">
  <div class="play"><svg width="20" height="22" viewBox="0 0 20 22"><polygon points="4,2 18,11 4,20" fill="#6b2fe6"/></svg></div>
</div>
<div class="video" style="left:615px;background:linear-gradient(150deg,#9a8874,#4f4a4a 60%,#2f2c2d)" role="img" aria-label="Video still of coworkers laughing around a laptop">
  <div class="play"><svg width="20" height="22" viewBox="0 0 20 22"><polygon points="4,2 18,11 4,20" fill="#6b2fe6"/></svg></div>
</div>

<section class="clients">
  <h2 class="section-title" style="top:68px">WHAT OUR CLIENTS SAY</h2>
  <div class="arrow" style="left:94px"><svg width="20" height="16" viewBox="0 0 20 16" fill="none" stroke="#6b2fe6" stroke-width="2"><line x1="18" y1="8" x2="3" y2="8"/><polyline points="9,2 3,8 9,14"/></svg></div>
  <div class="arrow" style="left:1064px"><svg width="20" height="16" viewBox="0 0 20 16" fill="none" stroke="#6b2fe6" stroke-width="2"><line x1="2" y1="8" x2="17" y2="8"/><polyline points="11,2 17,8 11,14"/></svg></div>
  <p class="quote">“Lorem ipsum dolor sit amet, consectetur adipiscing elit, sed do eiusmod tempor incididunt ut labore et dolore magna aliqua. Quis ipsum suspendisse ultrices gravida. Risus commodo viverra maecenas accumsan lacus vel facilisis. ”</p>
  <div class="avatar" role="img" aria-label="Client portrait"></div>
  <div class="who"><b>- Dana Whitlow</b><span>Lorem ipsum dolor</span></div>
</section>

<h2 class="section-title" style="top:3420px">LATEST BLOG</h2>
<article class="post" style="left:100px">
  <div class="photo" role="img" aria-label="Screenshot of an SEO report dashboard" style="background:linear-gradient(135deg,#f4f4f8,#c9d3ea 60%,#7fa67f)"></div>
  <div class="date">August 24 ,2022</div>
  <h3>Cost of Search SEO Report – Riverton, WI – Chiropractor</h3>
  <p>https://vid.example/Qe7Lm30rTz to give you an idea of what to expect. Uh, chose Riverton Wisconsin,</p>
  <div class="more">Learn More »</div>
</article>
<article class="post" style="left:442px">
  <div class="photo" role="img" aria-label="Photo of hands on a laptop with network icons" style="background:linear-gradient(150deg,#d9d4cf,#8c817b 60%,#4a4442)"></div>
  <div class="date">August 24 ,2022</div>
  <h3>Cost of Search SEO Report – Riverton, WI – Chiropractor</h3>
  <p>https://vid.example/Qe7Lm30rTz to give you an idea of what to expect. Uh, chose Riverton Wisconsin,</p>
  <div class="more">Learn More »</div>
</article>
<article class="post" style="left:784px">
  <div class="photo" role="img" aria-label="Photo of a laptop beside a glowing software graphic" style="background:linear-gradient(150deg,#2a3d52,#142230 60%,#0c1620)"></div>
  <div class="date">August 24 ,2022</div>
  <h3>Cost of Search SEO Report – Riverton, WI – Chiropractor</h3>
  <p>https://vid.example/Qe7Lm30rTz to give you an idea of what to expect. Uh, chose Riverton Wisconsin,</p>
  <div class="more">Learn More »</div>
</article>

<section class="contact">
  <div class="contact-photo" role="img" aria-label="Photo of hands resting near a laptop keyboard"></div>
  <div class="contact-leaf" role="img" aria-label="Green plant leaves"></div>
  <h2>CONTACT US</h2>
  <p class="lead">Lorem ipsum dolor sit amet, consectetur adipiscing elit, sed do</p>
  <div class="field" style="left:100px;top:256px;width:312px">Name*</div>
  <div class="field" style="left:421px;top:256px;width:313px">Phone*</div>
  <div class="field" style="left:100px;top:318px;width:312px">Email*</div>
  <div class="field" style="left:421px;top:318px;width:313px">Company*</div>
  <div class="field" style="left:100px;top:379px;width:634px;height:103px">Comments*</div>
  <div class="btn btn-primary" style="left:100px;top:498px;width:160px;height:39px;border:none">Submit Now »</div>
</section>

<footer class="footer">
  <div class="brand" style="left:102px;top:62px">
    <div class="brand-name">BRIGHT PEBBLES.info</div>
    <div class="brand-tag">Cutting Edge Business Services to Help You Shine Bright</div>
  </div>
  <div class="social" style="left:198px"></div>
  <div class="social" style="left:246px"></div>
  <div class="social" style="left:295px"></div>

  <div class="col" style="left:523px">
    <h4>Navigation</h4>
    <ul><li>Home</li><li>Shop</li><li>Solutions</li><li>Blog</li><li>Contact</li></ul>
  </div>
  <div class="col" style="left:716px">
    <h4>Contact Us</h4>
    <div class="info"><svg width="10" height="14" viewBox="0 0 10 14"><path d="M5 0a5 5 0 0 1 5 5c0 4-5 9-5 9S0 9 0 5a5 5 0 0 1 5-5z" fill="#fff"/><circle cx="5" cy="5" r="2" fill="#1b0f3b"/></svg><div>Address:<br>Fernbrook, WI, US 54012</div></div>
    <div class="info"><svg width="12" height="12" viewBox="0 0 12 12"><path d="M2 0l3 3-2 2c1 2 2 3 4 4l2-2 3 3-2 2C5 12 0 7 0 2z" fill="#fff"/></svg><div>Phone:<br>admin@brightpebbles.info</div></div>
    <div class="info"><svg width="13" height="10" viewBox="0 0 13 10"><rect width="13" height="10" fill="#fff"/><polyline points="0,0 6.5,6 13,0" fill="none" stroke="#1b0f3b" stroke-width="1.4"/></svg><div>Email:<br>admin@brightpebbles.info</div></div>
  </div>
  <div class="col" style="left:1003px">
    <h4>Resources</h4>
    <ul><li>Resources</li><li>Privacy Policy</li><li>Sitemap</li><li>Infographics</li><li>Press</li></ul>
  </div>
  <div class="top-btn"><svg width="16" height="18" viewBox="0 0 16 18" fill="none" stroke="#fff" stroke-width="2"><line x1="8" y1="17" x2="8" y2="2"/><polyline points="2,8 8,2 14,8"/></svg></div>
  <div class="top-label">BACK TO TOP</div>
  <div class="rule"></div>
  <div class="copy">Copyright ©2022 brightpebbles.info. All Rights Reserved.</div>
</footer>

</body>
</html>
```